LEAP GLIDE SOAR

Need a 4 X 6 post card design. Here are the elements that need to be on the card:
LEAP, GLIDE, SOAR (This is the title please feel free and create)
DATE: August 28, 2022
Showtimes 2:30 PM & 7:30 PM
Location: Harriet Colvane Theatre Walnut Creek, CA
Tickets can be purchased at:
http://colvanestagehall.tixora-example.com/LEAPGLIDESOAR or
by calling the ticket office at (925) 555-STAGE
LEAP, GLIDE, SOAR showcases the dance stylings of urban hip hop, ballet, modern jazz and much much more! Bay Area renown dancer/choreographer Rosa Janelle Pruitt headlines this cast of dancers and will amaze you as she takes you on a journey through dance that you will never forget. Join us for an experience that will prove to excite and delight you!
Now for the artwork I would like to incorporate all three of these photos. The photo entitled "beach" you are only to use the dancer on the left. So clip out the other dancer in the pink dress. The Garden photo and the beach photo the images need to be cut out from the background. The sidewalk photo you can leave the background (just my preference) but for the sake of the overall design I'm ok with removing its background as well.
Ok have at it. I want to end this competition in a few days so let's get these designs in. Thank you!

```html
<!DOCTYPE html>
<html lang="en">
<head>
<meta charset="utf-8">
<title>Leap Glide Soar – Postcard</title>
<link rel="stylesheet" href="https://fonts.googleapis.com/css2?family=Anton&family=Great+Vibes&family=Roboto+Condensed:wght@400;700&display=swap">
<style>
  :root {
    --page-bg: #e7e7ea;
    --ink-black: #0c0a0e;
    --panel-dark: #1a1420;
    --stage-deep: #2a0f3a;
    --stage-mid: #5a2478;
    --stage-glow: #9a4bb8;
    --hot-pink: #e0187a;
    --soft-white: #ffffff;
    --paper: #f3f3f5;
    --grey-band: #3a3a40;
    --text-dark: #1b1b1f;
    --rule: #b9b9c0;
    --script: "Great Vibes", cursive;
    --display: "Anton", sans-serif;
    --body: "Roboto Condensed", sans-serif;
  }
  * { box-sizing: border-box; margin: 0; padding: 0; }
  html, body { width: 900px; height: 1200px; overflow: hidden; }
  body { background: var(--page-bg); font-family: var(--body); position: relative; }

  .postcard {
    position: absolute; left: 54px; width: 792px; height: 476px;
    overflow: hidden; background: var(--paper);
    box-shadow: 0 6px 18px rgba(0,0,0,.18);
  }
  .postcard--front { top: 70px; }
  .postcard--back { top: 640px; background: var(--soft-white); }
  .abs { position: absolute; }

  /* Front */
  .front-panel {
    left: 0; top: 0; width: 274px; height: 476px;
    background: linear-gradient(180deg, #050406 0%, #121015 70%, #1d1b20 100%);
  }
  .front-photo {
    left: 274px; top: 0; width: 518px; height: 476px;
    background:
      radial-gradient(ellipse at 55% 35%, var(--stage-glow) 0%, var(--stage-mid) 35%, var(--stage-deep) 75%),
      var(--stage-deep);
  }
  .title { left: 0; top: 0; width: 274px; }
  .title__script { font-family: var(--script); color: var(--hot-pink); font-size: 56px; line-height: 1; position: absolute; }
  .title__bold {
    font-family: var(--display); color: var(--soft-white); font-size: 62px; line-height: 1;
    letter-spacing: 1px; position: absolute; text-shadow: 3px 3px 0 var(--hot-pink);
  }
  .front .title__script--top { left: 30px; top: 22px; }
  .front .title__bold { left: 30px; top: 80px; }
  .front .title__script--bottom { left: 120px; top: 140px; }

  .date-banner {
    background: var(--hot-pink); color: var(--soft-white);
    font-family: var(--body); font-weight: 700; font-size: 22px; letter-spacing: .5px;
    height: 31px; line-height: 31px; text-align: center;
    clip-path: polygon(0 0, 100% 0, 96% 50%, 100% 100%, 0 100%, 4% 50%);
  }
  .front .date-banner { left: 27px; top: 207px; width: 222px; }
  .showtimes { left: 0; width: 274px; top: 246px; text-align: center; color: var(--soft-white); font-weight: 700; font-size: 16px; }
  .rule { height: 1px; background: linear-gradient(90deg, transparent, var(--hot-pink), transparent); }
  .front .rule--one { left: 24px; width: 226px; top: 276px; }
  .front .rule--two { left: 24px; width: 226px; top: 336px; background: linear-gradient(90deg, transparent, var(--rule), transparent); }
  .venue { left: 0; width: 274px; top: 287px; text-align: center; color: var(--soft-white); font-weight: 700; font-size: 15px; line-height: 20px; }

  .swoosh { left: 0; top: 0; width: 792px; height: 476px; }

  .join-us { font-family: var(--script); color: var(--hot-pink); font-size: 34px; line-height: 1; }
  .join-copy { color: var(--soft-white); font-size: 14px; line-height: 18px; }
  .front .join-us { left: 12px; top: 392px; }
  .front .join-copy { left: 32px; top: 428px; }

  .tickets { text-align: center; }
  .tickets__label { color: var(--hot-pink); font-weight: 700; font-size: 12px; letter-spacing: .3px; }
  .tickets__url { color: var(--text-dark); font-weight: 700; font-size: 12px; margin-top: 2px; }
  .tickets__phone { color: var(--text-dark); font-size: 10px; margin-top: 1px; }
  .front .tickets { left: 470px; width: 314px; top: 420px; }
  .front .tickets__label { font-size: 11px; }
  .front .tickets__url { font-size: 11px; }
  .front .tickets__phone { font-size: 9.5px; }

  .venue-mark { right: 16px; top: 12px; display: flex; align-items: center; gap: 6px; }
  .venue-mark__square { width: 18px; height: 18px; background: var(--hot-pink); }
  .venue-mark__name { font-family: var(--body); font-weight: 700; font-size: 10px; line-height: 11px; color: var(--soft-white); width: 70px; }

  /* Back */
  .back-art { left: 0; top: 0; width: 792px; height: 476px; }
  .back .title__script--top { left: 28px; top: 28px; }
  .back .title__bold { left: 28px; top: 86px; }
  .back .title__script--bottom { left: 120px; top: 146px; }
  .back-dancer {
    left: 243px; top: 42px; width: 168px; height: 190px;
    background: linear-gradient(180deg, rgba(150,110,210,.85) 0%, rgba(240,236,244,.9) 40%, rgba(230,226,236,.4) 100%);
    border-radius: 40px 40px 10px 10px;
  }
  .back .date-banner { left: 24px; top: 202px; width: 225px; }
  .blurb { left: 24px; top: 244px; width: 330px; color: var(--soft-white); font-size: 11.5px; line-height: 14px; }
  .blurb p + p { margin-top: 10px; }
  .back .join-us { left: 24px; top: 342px; }
  .back .join-copy { left: 24px; top: 380px; font-size: 12.5px; }
  .back .tickets { left: 10px; width: 420px; top: 421px; }

  .mailing-address { left: 463px; top: 46px; color: var(--text-dark); font-size: 12px; line-height: 15px; }
  .stamp-box { left: 614px; top: 32px; width: 84px; height: 63px; border: 1px solid var(--rule); }
  .address-line { left: 431px; width: 267px; height: 1px; background: var(--rule); }
</style>
</head>
<body>

<section class="postcard postcard--front front" aria-label="Postcard front">
  <div class="abs front-photo" role="img" aria-label="Three dancers on a purple stage with sparkling lights: one in white with a violet scarf, one in a pink gown, one in black mid-leap"></div>
  <div class="abs front-panel"></div>

  <div class="abs venue-mark">
    <span class="venue-mark__square"></span>
    <span class="venue-mark__name">Colvane Center for the Arts</span>
  </div>

  <h1 class="abs title">
    <span class="title__script title__script--top">Leap</span>
    <span class="title__bold">GLIDE</span>
    <span class="title__script title__script--bottom">soar</span>
  </h1>

  <div class="abs date-banner">AUGUST 28, 2022</div>
  <p class="abs showtimes">Showtimes: 2:30 PM &amp; 7:30 PM</p>
  <div class="abs rule rule--one"></div>
  <p class="abs venue">Harriet Colvane Theatre<br>Walnut Creek, CA</p>
  <div class="abs rule rule--two"></div>

  <svg class="abs swoosh" viewBox="0 0 792 476" aria-hidden="true">
    <defs>
      <linearGradient id="greyBand" x1="0" y1="0" x2="1" y2="1">
        <stop offset="0" stop-color="#4a4a52"/>
        <stop offset="1" stop-color="#1c1c20"/>
      </linearGradient>
    </defs>
    <path d="M0,384 C120,344 250,352 380,476 L0,476 Z" fill="url(#greyBand)"/>
    <path d="M0,384 C120,344 250,352 380,476" fill="none" stroke="#ffffff" stroke-width="4"/>
    <path d="M0,376 C130,330 270,342 398,476" fill="none" stroke="#e0187a" stroke-width="6"/>
    <path d="M392,476 C470,420 620,392 792,384 L792,476 Z" fill="#f3f3f5"/>
    <path d="M392,476 C470,420 620,392 792,384" fill="none" stroke="#e0187a" stroke-width="7"/>
  </svg>

  <p class="abs join-us">Join us</p>
  <p class="abs join-copy">for an experience that will<br>prove to excite and delight you!</p>

  <div class="abs tickets">
    <p class="tickets__label">TICKETS CAN BE PURCHASED AT:</p>
    <p class="tickets__url">http://colvanestagehall.tixora-example.com/LEAPGLIDESOAR</p>
    <p class="tickets__phone">or by calling the ticket office at (925) 555-STAGE</p>
  </div>
</section>

<section class="postcard postcard--back back" aria-label="Postcard back">
  <svg class="abs back-art" viewBox="0 0 792 476" aria-hidden="true">
    <defs>
      <radialGradient id="stageBack" cx=".35" cy=".35" r=".8">
        <stop offset="0" stop-color="#5a2478"/>
        <stop offset=".5" stop-color="#2e1240"/>
        <stop offset="1" stop-color="#120818"/>
      </radialGradient>
    </defs>
    <path d="M0,0 L380,0 C500,120 560,300 520,410 L0,410 Z" fill="url(#stageBack)" role="img" aria-label="Dark purple stage backdrop with sparkles"/>
    <path d="M380,0 C500,120 560,300 520,410" fill="none" stroke="#ffffff" stroke-width="8"/>
    <path d="M392,0 C514,120 576,300 552,476" fill="none" stroke="#e0187a" stroke-width="9"/>
    <path d="M0,410 L520,410 L548,476 L0,476 Z" fill="#f3f3f5"/>
  </svg>

  <div class="abs back-dancer" role="img" aria-label="Dancer in white raising a violet scarf overhead"></div>

  <h2 class="abs title">
    <span class="title__script title__script--top">Leap</span>
    <span class="title__bold">GLIDE</span>
    <span class="title__script title__script--bottom">soar</span>
  </h2>

  <div class="abs date-banner">AUGUST 28, 2022</div>

  <div class="abs blurb">
    <p>LEAP, GLIDE, SOAR showcases the dance stylings of urban hip hop, ballet, modern jazz and much much more!</p>
    <p>Bay Area renown dancer/choreographer Rosa Janelle Pruitt headlines this cast of dancers and will amaze you as she takes you on a journey through dance that you will never forget.</p>
  </div>

  <p class="abs join-us">Join us</p>
  <p class="abs join-copy">for an experience that will prove to excite and delight you!</p>

  <div class="abs tickets">
    <p class="tickets__label">TICKETS CAN BE PURCHASED AT:</p>
    <p class="tickets__url">http://colvanestagehall.tixora-example.com/LEAPGLIDESOAR</p>
    <p class="tickets__phone">or by calling the ticket office at (925) 555-STAGE</p>
  </div>

  <p class="abs mailing-address">Harriet Colvane Theatre<br>Walnut Creek, CA</p>
  <div class="abs stamp-box"></div>
  <div class="abs address-line" style="top:228px"></div>
  <div class="abs address-line" style="top:262px"></div>
  <div class="abs address-line" style="top:298px"></div>
  <div class="abs address-line" style="top:332px"></div>
</section>

</body>
</html>
```